【社会貢献に繋がるお仕事です。ぜひ多数の方のご提案をよろしくお願いいたします。】

ユメヅキミナセのポスターデザインの作成をお願いします(イラスト入りで)。
ユメヅキとは、
「ユメヅキ」とは「ユメノツキアカリ」の略で、「地域をランニングして見回ることで安全で暮らしやすい街にする取り組み」のこと。ランニングという日常的な趣味を防犯パトロールという社会貢献に活かそうというものです。
詳しくは公式サイトをご参照ください。
http://yumezk.o-hana.example/
ユメヅキとは
http://yumezk.o-hana.example/meaning/

A2サイズ、片面カラー
Illustrator形式(CS5)

全体のベースカラーは赤で。

メインのイラスト(オリジナルで)。=赤いパトランTシャツ(写真参照)と腕章(「防犯」の文字)を着用したランナー数名が楽しそうに走っている姿を中心に、あとはお任せ。

●タイトル「ユメヅキミナセ メンバー大募集!」(大きめの文字サイズ)

●キャッチフレーズ「走って奏でる、地域の安心。」(大きめの文字サイズ)

●文章:「仲間と楽しく走って、地域貢献しませんか?」(少し大きめの文字サイズ)

●文章:「ユメヅキ」とは「ユメノツキアカリ」の略で、地域を走りながらパトロールすることで安全で暮らしやすい街にすること。ランニングという日常的な趣味を防犯という社会貢献に活かそうというものです。

●文章:
こんな方におすすめ!
・健康、ダイエット、ストレス解消などのために運動したい方
・夜でも安心して走りたい女性の方
・地域社会に貢献したい方
・ジョギング仲間がほしい方

●ユメヅキのロゴ(添付ファイル参照)

●「参加無料」の表示
●「ユメヅキミナセ」での検索ボックスと「詳しくは『ユメヅキミナセ』で検索!」の文字
●公式サイト(http://yumezk.o-hana.example/)のURLとQRコード

●詳細情報:

【活動内容】
主に夜間、1班数名程度のチームでゆっくりと走りながら街を見回ります。ご希望の方に専用Tシャツ(購入・着用は任意)を有償配布しています。
【活動地域・日程】
北九州市内(及び周辺)の各地。詳細と日程は公式サイトでご確認ください。
【参加資格】
18歳以上の男女。ランニング未経験者も大歓迎。会員登録が必要です。詳しくは公式サイトでご確認ください。

●添付の写真(2枚)をどこかに挿入してください。
松浦さんの写真のほうは人物のみ切り抜いて使用。近くに小さく「ユメヅキミナセ会員兼特別アドバイザー松浦千景さん(1992年ヴェルダ国際競技会日本代表)」と記載。

●運営者情報:

ユメヅキミナセ 担当:(代表)杉野 (副代表)早乙女、柳瀬
運営:NPO法人全国アクティブライフ振興会
連絡先:090-2763-4091(杉野)
※ ユメヅキミナセは、NPO法人みらい創造ネット(宗像市)が運営するユメヅキJAPANに加盟しています。

メインのイラストのクオリティが非常に高く、また、爽やかなユメヅキのイメージにピッタリなので選びました。

皆様、素晴らしいご提案を、本当にありがとうございました。
非常にレベルの高いご提案ばかりで、理事会での選定にかなり時間を要してしまいました。
今回、ユメヅキミナセの最初のポスター作成になりますが、2回目以降のポスター作成の際にぜひ使わせていただきたくなるようなご提案もいくつかあります。
今後またコンペ、プロジェクト、仕事依頼などでクリエモールを利用させていただくと思いますので、どうぞよろしくお願いいたします。

```html
<!DOCTYPE html>
<html lang="ja">
<head>
<meta charset="utf-8">
<title>ユメヅキミナセ メンバー大募集</title>
<link rel="stylesheet" href="https://fonts.googleapis.com/css2?family=M+PLUS+Rounded+1c:wght@500;800;900&family=Noto+Sans+JP:wght@400;700;900&display=swap">
<style>
  :root {
    --red: #e60012;
    --red-deep: #b8000e;
    --white: #ffffff;
    --ink: #222222;
    --yellow: #ffe100;
    --photo-warm: #c9573f;
    --photo-soft: #d98a72;
    --photo-dark: #5a2a25;
  }
  * { margin: 0; padding: 0; box-sizing: border-box; }
  html, body { width: 849px; height: 1200px; overflow: hidden; background: var(--white); }
  .poster {
    position: relative; width: 849px; height: 1200px; overflow: hidden;
    background: var(--red);
    font-family: "Noto Sans JP", sans-serif; color: var(--ink);
  }
  .free-badge {
    position: absolute; left: 22px; top: 14px; width: 88px; height: 88px;
    border-radius: 50%; background: var(--yellow); color: var(--red);
    display: flex; flex-direction: column; align-items: center; justify-content: center;
    font-family: "M PLUS Rounded 1c", sans-serif; font-weight: 900; font-size: 24px; line-height: 1.05;
    transform: rotate(-12deg);
  }
  .recruit-heading {
    position: absolute; left: 0; right: 0; top: 16px; text-align: center;
    font-family: "M PLUS Rounded 1c", sans-serif; font-weight: 900; font-size: 56px;
    color: var(--white); letter-spacing: 2px;
  }
  .title-roman {
    position: absolute; left: 0; right: 0; top: 92px; text-align: center;
    font-family: "M PLUS Rounded 1c", sans-serif; font-weight: 800; font-size: 16px;
    color: var(--white); letter-spacing: 4px;
  }
  .title {
    position: absolute; left: 0; right: 0; top: 104px; text-align: center;
    font-family: "M PLUS Rounded 1c", sans-serif; font-weight: 900; font-size: 96px;
    color: var(--white); letter-spacing: -2px;
    transform: skewX(-10deg);
    text-shadow: 4px 4px 0 var(--red-deep);
  }
  .photo { position: absolute; }
  .photo--group { left: 40px; top: 430px; width: 770px; height: 270px; border-radius: 8px;
    background: linear-gradient(180deg, var(--photo-soft), var(--photo-warm) 60%, var(--photo-dark)); }
  .photo--advisor { left: 290px; top: 218px; width: 270px; height: 480px; border-radius: 130px 130px 10px 10px;
    background: linear-gradient(180deg, #3a2a30 0%, var(--photo-warm) 35%, var(--red) 75%, #2a2a2a 100%); }
  .info-box {
    position: absolute; background: var(--white); border-radius: 14px; padding: 14px 16px;
    font-size: 13.5px; line-height: 1.6;
  }
  .info-box h2 {
    font-family: "M PLUS Rounded 1c", sans-serif; font-weight: 900; font-size: 20px; color: var(--red); margin-bottom: 6px;
  }
  .info-box--about { left: 22px; top: 238px; width: 252px; height: 190px; }
  .info-box--recommend { left: 576px; top: 238px; width: 252px; height: 214px; }
  .info-box--recommend ul { list-style: none; }
  .info-box--recommend li { padding-left: 1em; text-indent: -1em; }
  .info-box--recommend li::before { content: "・"; color: var(--red); }
  .advisor-caption {
    position: absolute; left: 576px; top: 462px; width: 240px;
    font-size: 10px; line-height: 1.5; color: var(--white);
  }
  .bubble {
    position: absolute; background: var(--white); border-radius: 50%;
    display: flex; align-items: center; justify-content: center; text-align: center;
    font-family: "M PLUS Rounded 1c", sans-serif; font-weight: 900; font-size: 22px; color: var(--ink); line-height: 1.15;
  }
  .bubble--together { left: 160px; top: 580px; width: 118px; height: 76px; }
  .bubble--waiting { left: 418px; top: 470px; width: 150px; height: 64px; }
  .catch-band {
    position: absolute; left: -30px; top: 712px; width: 920px; height: 150px;
    background: var(--white); transform: rotate(-4deg);
    display: flex; flex-direction: column; justify-content: center; padding-left: 230px;
    font-family: "M PLUS Rounded 1c", sans-serif; font-weight: 900; color: var(--red);
  }
  .catch-band .catchphrase { font-size: 42px; }
  .catch-band .invite { font-size: 38px; margin-left: -150px; margin-top: 4px; }
  .details {
    position: absolute; left: 0; top: 880px; width: 849px; height: 320px; background: var(--white);
    padding: 18px 28px; font-size: 11px; line-height: 1.65;
  }
  .details .label { color: var(--red); font-weight: 700; }
  .operator { margin-top: 10px; padding-top: 8px; border-top: 2px solid var(--red); font-size: 11.5px; }
  .site-row { position: absolute; left: 28px; bottom: 22px; right: 28px; display: flex; align-items: center; gap: 16px; }
  .org-mark { display: flex; align-items: center; gap: 6px; font-weight: 700; font-size: 16px; color: var(--red); }
  .org-mark i { width: 16px; height: 16px; background: var(--red); display: block; }
  .site-links { flex: 1; }
  .site-url { font-weight: 700; font-size: 24px; color: var(--ink); }
  .site-url span { color: var(--red); font-size: 20px; margin-right: 10px; }
  .search-row { display: flex; align-items: center; gap: 8px; margin-top: 6px; font-weight: 700; font-size: 15px; }
  .search-box { border: 2px solid #999; padding: 3px 10px; width: 200px; font-weight: 400; }
  .search-button { background: #666; color: var(--white); padding: 4px 12px; font-size: 13px; border-radius: 3px; }
</style>
</head>
<body>
<main class="poster">
  <div class="free-badge"><span>参加</span><span>無料</span></div>
  <h1 class="recruit-heading">メンバー大募集！</h1>
  <p class="title-roman">YUMEZUKI MINASE</p>
  <p class="title">ユメヅキミナセ</p>

  <div class="photo photo--group" role="img" aria-label="赤いTシャツ姿のメンバーたちの集合写真"></div>
  <div class="photo photo--advisor" role="img" aria-label="帽子をかぶり赤いTシャツで走る松浦千景さんの切り抜き写真"></div>

  <section class="info-box info-box--about">
    <h2>「ユメヅキ」とは？</h2>
    <p>「ユメノツキアカリ」の略で、地域を走りながらパトロールすることで安全で暮らしやすい街にすること。ランニングという日常的な趣味を防犯という社会貢献に活かそうというものです。</p>
  </section>

  <section class="info-box info-box--recommend">
    <h2>こんなにおすすめ！</h2>
    <ul>
      <li>健康、ダイエット、ストレス解消などのために運動したい方</li>
      <li>夜でも安心して走りたい女性の方</li>
      <li>地域社会に貢献したい方</li>
      <li>ジョギング仲間がほしい方</li>
    </ul>
  </section>

  <p class="advisor-caption">ユメヅキミナセ会員兼特別アドバイザー 松浦千景さん（1992年ヴェルダ国際競技会日本代表）</p>

  <div class="bubble bubble--together">共に<br>走ろう！</div>
  <div class="bubble bubble--waiting">待ってまーす！</div>

  <div class="catch-band">
    <p class="catchphrase">走って奏でる、地域の安心。</p>
    <p class="invite">仲間と楽しく走って、地域貢献しませんか？</p>
  </div>

  <section class="details">
    <p><span class="label">【活動内容】</span>主に夜間、1班数名程度のチームでゆっくりと走りながら街を見回ります。ご希望の方に専用Tシャツ（購入・着用は任意）を有償配布しています。</p>
    <p><span class="label">【活動地域・日程】</span>北九州市内（及び周辺）の各地。詳細と日程は公式サイトでご確認ください。</p>
    <p><span class="label">【参加資格】</span>18歳以上の男女。ランニング未経験者も大歓迎。会員登録が必要です。詳しくは公式サイトでご確認ください。</p>
    <div class="operator">
      <p>運営者情報：ユメヅキミナセ　担当：（代表）杉野　（副代表）早乙女、柳瀬　運営：NPO法人全国アクティブライフ振興会</p>
      <p>連絡先：090-2763-4091（杉野）</p>
      <p>※ユメヅキミナセは、NPO法人みらい創造ネット（宗像市）が運営するユメヅキJAPANに加盟しています。</p>
    </div>
    <div class="site-row">
      <div class="org-mark"><i></i>ユメヅキ</div>
      <div class="site-links">
        <p class="site-url"><span>公式サイト</span>http://yumezk.o-hana.example/</p>
        <div class="search-row">
          <span class="search-box">ユメヅキミナセ</span>
          <span class="search-button">検索</span>
          <span>詳しくは「ユメヅキミナセ」で検索！</span>
        </div>
      </div>
    </div>
  </section>
</main>
</body>
</html>
```